Website design for company that sells taximeters and has a taxi dispatch call center, webstore neede

Need a website with a shop with at least 20 articles, in two languages, possibly by using a purchased theme (not purchased yet).The company provides equipments and dispatch solutions for taxi companies. Typical yellow and black theme

Target Market(s)

Taxi companies

Industry/Entity Type

Taxi

Number of Pages Required

3 page

Font styles to use
Sans Serif

Colors
fbed22
000000

Requirements
Must have
• - webstore for at least 20 articles
• - Documents folder where to put pdf material related to taximeters
• - contact form message submission
Nice to have
• Feedback section
Should not have
• Blogs,

```html
<!DOCTYPE html>
<html lang="en">
<head>
<meta charset="utf-8">
<title>Installers — Farevolt</title>
<link href="https://fonts.googleapis.com/css2?family=Open+Sans:wght@400;600;700;800&display=swap" rel="stylesheet">
<style>
  :root {
    --yellow: #fbd522;
    --band: #efc43f;
    --black: #0b0b0b;
    --ink: #333333;
    --grey: #7a7a7a;
    --num: #f6e0a6;
    --white: #ffffff;
  }
  * { margin: 0; padding: 0; box-sizing: border-box; }
  html, body { width: 850px; height: 1200px; overflow: hidden; }
  body {
    position: relative;
    font-family: "Open Sans", sans-serif;
    background: var(--white);
    color: var(--ink);
  }
  .hero {
    position: absolute; left: 0; top: 0; width: 850px; height: 203px;
    background:
      radial-gradient(circle at 25% 40%, rgba(214,120,40,.35), transparent 18%),
      radial-gradient(circle at 80% 25%, rgba(160,180,150,.3), transparent 16%),
      radial-gradient(circle at 45% 95%, rgba(220,170,60,.45), transparent 18%),
      linear-gradient(180deg, #1b2330 0%, #121822 60%, #1a1c20 100%);
  }
  .brand {
    position: absolute; left: 106px; top: 11px;
    font-size: 17px; font-weight: 800; letter-spacing: 1px; color: var(--yellow);
  }
  .nav {
    position: absolute; left: 271px; top: 15px; display: flex; gap: 5px;
    list-style: none; font-size: 7px; font-weight: 700; letter-spacing: .3px; color: var(--white);
  }
  .nav .active { color: var(--yellow); }
  .phone {
    position: absolute; left: 535px; top: 10px; display: flex; align-items: center; gap: 8px;
    font-size: 8px; font-weight: 700; letter-spacing: 1px; color: var(--yellow);
  }
  .lang { position: absolute; left: 629px; top: 13px; font-size: 7px; font-weight: 700; color: var(--white); }
  .search {
    position: absolute; left: 696px; top: 10px; width: 108px; height: 20px;
    border: 1.5px solid var(--yellow); border-radius: 10px;
    font-size: 9px; font-weight: 600; color: var(--white); letter-spacing: .5px;
    padding: 3px 0 0 11px;
  }
  .search svg { position: absolute; right: 8px; top: 4px; }
  .hero-title {
    position: absolute; left: 0; width: 875px; top: 82px; text-align: center;
    font-size: 20px; font-weight: 700; letter-spacing: 2.5px; color: var(--white);
  }
  .hero-sub {
    position: absolute; left: 0; width: 875px; top: 114px; text-align: center;
    font-size: 7.5px; font-weight: 700; letter-spacing: .8px; color: var(--white);
  }
  .intro-title {
    position: absolute; left: 0; width: 862px; top: 248px; text-align: center;
    font-size: 23px; font-weight: 700; letter-spacing: -1px; color: var(--ink);
  }
  .rule { position: absolute; left: 403px; top: 294px; width: 55px; height: 2px; background: var(--band); }
  .intro-text {
    position: absolute; left: 170px; width: 530px; top: 327px; text-align: center;
    font-size: 13px; line-height: 16.5px; color: var(--grey);
  }
  .step { position: absolute; top: 452px; width: 120px; }
  .step-num { font-size: 26px; font-weight: 700; color: var(--num); margin-left: 28px; line-height: 34px; }
  .step-text { margin-top: 6px; font-size: 13px; line-height: 19.4px; color: var(--grey); }
  .band {
    position: absolute; left: 0; top: 963px; width: 850px; height: 71px; background: var(--band);
    text-align: center; font-size: 22px; font-weight: 700; letter-spacing: -1px; color: var(--ink);
    padding-top: 20px;
  }
  .footer { position: absolute; left: 0; top: 1034px; width: 850px; height: 166px; background: var(--black); color: var(--white); }
  .foot-col { position: absolute; top: 28px; width: 125px; font-size: 6px; line-height: 10.5px; }
  .foot-col h4 { font-size: 6.5px; font-weight: 700; margin-bottom: 7px; }
  .foot-col h4 span, .foot-col .hl { color: var(--yellow); }
  .social { display: flex; gap: 4px; }
  .social i { display: block; width: 8px; height: 8px; border-radius: 50%; background: var(--white); }
  .foot-rule { position: absolute; left: 179px; top: 98px; width: 500px; height: 1px; background: #555; }
  .legal { position: absolute; left: 179px; top: 106px; font-size: 5.5px; }
  .legal .hl { color: var(--yellow); }
</style>
</head>
<body>
  <header class="hero" role="img" aria-label="Night city street with blurred lights and an illuminated taxi roof sign">
  </header>
  <div class="brand">FAREVOLT</div>
  <ul class="nav">
    <li class="active">HOME</li><li>SHOP</li><li>SERVICES</li><li>INSTALLERS</li><li>CONTACT US</li><li>JOIN US</li>
  </ul>
  <div class="phone">
    <svg width="13" height="13" viewBox="0 0 24 24" fill="none" stroke="#fff" stroke-width="1.6"><path d="M5 3h4l2 5-2.5 1.5a11 11 0 0 0 6 6L16 13l5 2v4a2 2 0 0 1-2 2A16 16 0 0 1 3 5a2 2 0 0 1 2-2z"/></svg>
    555.204.7781
  </div>
  <div class="lang">ENG v</div>
  <div class="search">search
    <svg width="10" height="10" viewBox="0 0 24 24" fill="none" stroke="#fff" stroke-width="2"><circle cx="10" cy="10" r="7"/><path d="M15 15l6 6"/></svg>
  </div>
  <h1 class="hero-title">INSTALLERS</h1>
  <p class="hero-sub">NOTHING IS DONE RIGHT, UNLESS IS DONE CORRECT.</p>

  <main>
    <h2 class="intro-title">Check out our list of authirized installers</h2>
    <div class="rule"></div>
    <p class="intro-text">Lorem ipsum dolor sit amet, consectetuer adipiscing elit. Aenean commodo ligula eget dolor. Aenean massa. Cum sociis natoque penatibus et magnis dis parturient montes, nascetur ridiculus mus. Donec qu</p>

    <section class="step" style="left:133px">
      <div class="step-num">1</div>
      <p class="step-text">Lorem ipsum dolor sit amet, consectetuer adipiscing elit. Aenean commodo ligula eget dolor. Aenean massa. Cum sociis natoque penatibus et magnis dis parturient montes, nascetur ridiculus mus. Donec qu</p>
    </section>
    <section class="step" style="left:371px">
      <div class="step-num">2</div>
      <p class="step-text" style="margin-top:4px">Lorem ipsum dolor sit amet, consectetuer adipiscing elit. Aenean commodo ligula eget dolor. Aenean massa. Cum sociis natoque penatibus et magnis dis parturient montes, nascetur ridiculus mus. Donec qu</p>
    </section>
    <section class="step" style="left:622px">
      <div class="step-num">3</div>
      <p class="step-text">Lorem ipsum dolor sit amet, consectetuer adipiscing elit. Aenean commodo ligula eget dolor. Aenean massa. Cum sociis natoque penatibus et magnis dis parturient montes, nascetur ridiculus mus. Donec qu</p>
    </section>
  </main>

  <div class="band">We only work with the best!</div>

  <footer class="footer">
    <div class="foot-col" style="left:179px">
      <h4>ABOUT <span>FAREVOLT</span></h4>
      <p>We provide quality dispatch and meter equipment for indecent taxi &amp; fleet vendors.</p>
    </div>
    <div class="foot-col" style="left:307px">
      <h4>CONTACT INFO</h4>
      <p>Shop Office: (555) 314-2260<br>Customer service: (555) 867-1093<br>Email: <span class="hl">hello@farevolt.example</span></p>
    </div>
    <div class="foot-col" style="left:435px">
      <h4>HOURS OF SERVICE</h4>
      <p>Monday - Friday: 09:00AM - 09:00PM<br>Saturday: 09:00AM - 07:00PM<br>Sunday: Closed</p>
    </div>
    <div class="foot-col" style="left:562px">
      <h4>LINK <span>US</span></h4>
      <div class="social"><i></i><i></i><i></i><i></i><i></i></div>
    </div>
    <div class="foot-rule"></div>
    <p class="legal">© 2018 <span class="hl">Farevolt.example</span> &nbsp;&nbsp;&nbsp;&nbsp;&nbsp;| &nbsp;Trademarks and brands are the property of their respective owners.</p>
  </footer>
</body>
</html>
```